Wrap needed for mobile fleet washing service

We need a wrap design for the mobile fleet washing division of our company, Brisq. We send crews of guys to our customers' locations to wash their fleet vehicles with pressure washers and chemicals, so they don't have to wash their vehicles themselves. We wash dump trucks, tractor-trailers, and garbage trucks, primarily. The wrap needs to fit a 2017 Kelu cabover truck with an 18 foot box on it. Wrap needs to be clean, modern, and professional.
Target Market(s)
Businesses with fleets-- hauling companies, garbage companies, trucking companies.
Industry/Entity Type
Service, Transportation

```html
<!DOCTYPE html>
<html lang="en">
<head>
<meta charset="utf-8">
<title>Brisq Fleet Washing Service – Box Truck Wrap</title>
<link rel="stylesheet" href="https://fonts.googleapis.com/css2?family=Roboto:wght@500;700;900&display=swap">
<style>
  :root {
    --canvas-bg: #e9ecef;
    --navy: #0a1633;
    --sky: #2b9fd9;
    --sky-light: #3aa9e0;
    --text-light: #e9eff6;
    --text-list: #e3f1fb;
    --photo-light: #d9dde2;
    --photo-mid: #9aa1aa;
    --photo-red: #c7545d;
  }
  html, body {
    margin: 0;
    padding: 0;
    width: 1200px;
    height: 900px;
    overflow: hidden;
    background: var(--canvas-bg);
    font-family: "Roboto", Arial, sans-serif;
  }
  .wrap-panel {
    position: absolute;
    left: 20px;
    top: 178px;
    width: 1160px;
    height: 544px;
    background: var(--navy);
    overflow: hidden;
  }
  .wrap-art {
    position: absolute;
    inset: 0;
    width: 100%;
    height: 100%;
  }
  .brand-name {
    position: absolute;
    left: 54px;
    top: 22px;
    margin: 0;
    font-family: "Roboto", Arial, sans-serif;
    font-weight: 500;
    font-size: 150px;
    line-height: 1;
    letter-spacing: -2px;
    color: var(--sky);
  }
  .service-title {
    position: absolute;
    left: 103px;
    top: 205px;
    margin: 0;
    font-weight: 700;
    font-size: 45px;
    line-height: 57px;
    color: var(--text-light);
    text-transform: uppercase;
  }
  .service-summary {
    position: absolute;
    left: 103px;
    top: 388px;
    margin: 0;
    font-weight: 700;
    font-size: 12px;
    line-height: 14px;
    color: var(--text-light);
    text-transform: uppercase;
    letter-spacing: -0.2px;
  }
  .contact-phone {
    position: absolute;
    left: 100px;
    top: 458px;
    display: flex;
    align-items: center;
    gap: 16px;
    font-weight: 700;
    font-size: 47px;
    color: #fff;
    letter-spacing: 0.5px;
  }
  .contact-phone svg { width: 42px; height: 42px; }
  .vehicle-list {
    position: absolute;
    left: 938px;
    top: 222px;
    margin: 0;
    padding: 0;
    list-style: none;
    color: var(--text-list);
    font-weight: 700;
    text-transform: uppercase;
  }
  .vehicle-list .list-heading {
    font-size: 32px;
    line-height: 1;
    margin-bottom: 14px;
  }
  .vehicle-list li {
    font-size: 20px;
    line-height: 38px;
  }
</style>
</head>
<body>
  <section class="wrap-panel">
    <svg class="wrap-art" viewBox="0 0 1238 580" preserveAspectRatio="none" aria-hidden="false">
      <defs>
        <linearGradient id="washPhotoTone" x1="0" y1="0" x2="0.3" y2="1">
          <stop offset="0" stop-color="#8a7f70"/>
          <stop offset="0.25" stop-color="var(--photo-light)"/>
          <stop offset="0.55" stop-color="var(--photo-red)"/>
          <stop offset="0.75" stop-color="var(--photo-light)"/>
          <stop offset="1" stop-color="#3a3e45"/>
        </linearGradient>
        <clipPath id="hexCluster">
          <polygon points="768,105 820,14 926,14 978,105 926,196 820,196"/>
          <polygon points="595,200 647,109 753,109 805,200 753,291 647,291"/>
          <polygon points="768,295 820,204 926,204 978,295 926,386 820,386"/>
          <polygon points="595,390 647,299 753,299 805,390 753,481 647,481"/>
          <polygon points="768,485 820,394 926,394 978,485 926,576 820,576"/>
        </clipPath>
      </defs>
      <!-- light blue right field -->
      <polygon class="sky-field" fill="var(--sky)"
        points="930,0 1238,0 1238,580 930,580 978,485 930,400 978,295 930,210 978,105 930,20"/>
      <!-- hexagon frames -->
      <g class="hex-frames" fill="var(--sky-light)">
        <polygon points="756,105 814,4 932,4 990,105 932,206 814,206"/>
        <polygon points="583,200 641,99 759,99 817,200 759,301 641,301"/>
        <polygon points="756,295 814,194 932,194 990,295 932,396 814,396"/>
        <polygon points="583,390 641,289 759,289 817,390 759,491 641,491"/>
        <polygon points="756,485 814,384 932,384 990,485 932,586 814,586"/>
      </g>
      <g class="hex-photo" role="img" aria-label="Photo of a foam-covered red truck being pressure washed in a wash bay">
        <rect x="580" y="0" width="420" height="580" fill="url(#washPhotoTone)" clip-path="url(#hexCluster)"/>
      </g>
    </svg>

    <h1 class="brand-name">Brisq</h1>

    <h2 class="service-title">Fleet<br>Washing<br>Service</h2>

    <p class="service-summary">
      We send crews of guys<br>
      to our customers' locations<br>
      to wash their fleet vehicles<br>
      with pressure washers and chemicals
    </p>

    <div class="contact-phone">
      <svg viewBox="0 0 48 48" aria-hidden="true">
        <path fill="#fff" d="M14 6c-1.5 0-3 .6-4.2 1.8L7 10.6c-2.6 2.6-2.3 9 4.6 17.4 7.5 9.1 15.2 13.5 19.2 11.6 1-.5 2.6-2.1 3.7-3.3 1.4-1.5 1.3-3.7-.2-5l-4-3.3c-1.3-1-3.1-1-4.3.1l-2 1.8c-2.5-1.2-6.2-5.3-7.5-8l1.9-2c1.1-1.2 1.2-3 .2-4.3L15.4 6.7C15 6.3 14.5 6 14 6z"/>
        <path fill="none" stroke="#fff" stroke-width="3" stroke-linecap="round" d="M27 14a8 8 0 0 1 7 7M28 7a15 15 0 0 1 13 13M26 20.5a2.5 2.5 0 0 1 2 2"/>
      </svg>
      <span>000 000 0000</span>
    </div>

    <ul class="vehicle-list">
      <li class="list-heading">We Wash</li>
      <li>Tractor-Trailers</li>
      <li>Dump Trucks</li>
      <li>Garbage Trucks</li>
    </ul>
  </section>
</body>
</html>
```